Oven Cleaning flyer design

Hi there,
I need help designing a letterbox flyer. It needs to be DL size.
I have attached a rough design made with Chat GPT.
Would like back and front, have my business colors.
Please find attached mock up of what I would roughly like.
Also find attached logo.
Thank you

Target Market(s)

Home owners over 40

Industry/Entity Type

Cleaning

Requirements
Must have
• Logo, before after of oven, brand colors

```html
<!DOCTYPE html>
<html lang="en">
<head>
<meta charset="utf-8">
<title>Gleam Oven Care – DL Flyer</title>
<link rel="stylesheet" href="https://fonts.googleapis.com/css2?family=Krona+One&family=Poppins:wght@400;600;700;800&family=Roboto+Condensed:wght@600&display=swap">
<style>
  :root {
    --teal: #47c3c9;
    --ink: #0d0d0d;
    --paper: #ffffff;
    --stage: #505050;
  }
  * { box-sizing: border-box; margin: 0; padding: 0; }
  html, body { width: 1200px; height: 1150px; overflow: hidden; }
  body { background: var(--stage); font-family: "Poppins", sans-serif; position: relative; }

  .flyer { position: absolute; top: 80px; width: 482px; height: 990px; overflow: hidden; }
  .flyer--front { left: 95px; background: var(--ink); }
  .flyer--back { left: 612px; background: var(--paper); }
  .flyer > * { position: absolute; }
  .backdrop { left: 0; top: 0; width: 482px; height: 990px; }

  .brand { left: 0; width: 100%; display: flex; align-items: center; justify-content: center; gap: 12px; }
  .brand__dot { width: 40px; height: 40px; border-radius: 50%; background: var(--teal); }
  .brand__name { font-family: "Poppins", sans-serif; font-weight: 700; font-size: 30px; color: var(--teal); letter-spacing: 0.5px; }
  .flyer--front .brand { top: 52px; }
  .flyer--back .brand { top: 44px; }

  .headline { left: 0; width: 100%; text-align: center; font-family: "Krona One", sans-serif; line-height: 1; }
  .headline span { display: block; }
  .headline--front { top: 170px; font-size: 38px; color: var(--paper); }
  .headline--front span { margin-bottom: 9px; }
  .headline--front .accent { color: var(--teal); }

  .intro { left: 68px; top: 325px; width: 333px; height: 218px; background: var(--teal); border-radius: 12px;
    color: var(--paper); font-weight: 700; font-size: 18.5px; line-height: 29px; text-align: center; padding-top: 13px; z-index: 2; }

  .compare { left: 26px; top: 509px; width: 429px; height: 251px; background: var(--paper); border-radius: 24px; padding: 6px; display: flex; gap: 12px; }
  .compare__shot { flex: 1; height: 100%; }
  .compare__shot--before { border-radius: 18px 0 0 18px; background: radial-gradient(circle at 50% 35%, #d49a3a 0%, #8a5418 45%, #3a2810 100%); }
  .compare__shot--after { border-radius: 0 18px 18px 0; background: radial-gradient(circle at 50% 35%, #4a5a6e 0%, #1f2834 55%, #0f141b 100%); }

  .tag { top: 771px; height: 33px; color: var(--paper); font-weight: 700; font-size: 22px; line-height: 33px; text-align: center;
    background: linear-gradient(90deg, rgba(13,13,13,0) 0%, var(--ink) 18%, var(--ink) 82%, rgba(13,13,13,0) 100%); }
  .tag--before { left: 49px; width: 168px; }
  .tag--after { left: 241px; width: 199px; }

  .cta-lead { left: 0; width: 100%; top: 832px; text-align: center; font-weight: 700; font-size: 20px; color: var(--ink); }
  .cta-main { left: 0; width: 100%; top: 868px; text-align: center; font-weight: 700; font-size: 27px; color: var(--paper); letter-spacing: 0.3px; }

  .phone { display: flex; align-items: center; gap: 8px; font-family: "Roboto Condensed", sans-serif; font-weight: 600; }
  .phone__icon { width: 52px; height: 52px; border-radius: 50%; background: var(--paper); display: flex; align-items: center; justify-content: center; flex: none; }
  .phone--front { left: 49px; top: 906px; font-size: 56px; color: var(--ink); }

  .headline--back { top: 148px; color: var(--teal); font-size: 36px; }
  .headline--back .sub { color: var(--ink); font-size: 22px; margin-top: 8px; }

  .reasons { left: 36px; top: 256px; width: 430px; list-style: none; font-weight: 600; font-size: 14.6px; line-height: 18px; color: var(--ink); }
  .reasons li { display: flex; gap: 10px; margin-bottom: 16px; }
  .reasons li::before { content: ""; flex: none; width: 18px; height: 18px; border-radius: 50%; background: var(--teal); margin-top: 1px; }

  .offer-lead { left: 0; width: 100%; top: 547px; text-align: center; font-size: 28px; color: var(--ink); }
  .offer-main { left: 0; width: 100%; top: 584px; text-align: center; font-weight: 700; font-size: 37px; color: var(--paper); }

  .perks { left: 0; top: 643px; width: 100%; display: flex; justify-content: space-around; padding: 0 18px; }
  .perk { width: 140px; text-align: center; }
  .perk__badge { width: 102px; height: 102px; margin: 0 auto; border-radius: 50%; background: var(--ink); border: 3px solid var(--ink);
    box-shadow: inset 0 0 0 3px var(--teal); display: flex; align-items: center; justify-content: center; }
  .perk__label { margin-top: 14px; font-weight: 800; font-size: 17.5px; line-height: 21px; color: var(--paper); }

  .contact { left: 25px; top: 817px; width: 432px; height: 118px; background: var(--ink); border-radius: 16px; }
  .phone--back { position: absolute; left: 36px; top: 8px; font-size: 52px; color: var(--paper); }
  .phone--back .phone__icon { background: var(--teal); }
  .contact__web { position: absolute; left: 0; width: 100%; top: 66px; text-align: center; font-size: 28px; font-weight: 600; color: var(--teal); }

  .footnote { left: 0; width: 100%; top: 941px; text-align: center; font-family: "Roboto Condensed", sans-serif; font-weight: 600; font-size: 19px; color: var(--paper); }
</style>
</head>
<body>

<section class="flyer flyer--front">
  <svg class="backdrop" viewBox="0 0 482 990" aria-hidden="true">
    <path d="M0 655 Q260 620 482 483 L482 990 L0 990 Z" fill="var(--teal)"/>
  </svg>

  <div class="brand"><span class="brand__dot"></span><span class="brand__name">Gleam Oven Care</span></div>

  <h1 class="headline headline--front">
    <span>BRING YOUR</span>
    <span class="accent">OVEN BACK</span>
    <span>TO LIFE</span>
  </h1>

  <p class="intro">Professional,<br>Non-caustic oven cleaning<br>that removes built-up grease,<br>smoke,and burnt grime<br>leaving your<br>oven looking fresh again.</p>

  <div class="compare">
    <div class="compare__shot compare__shot--before" role="img" aria-label="Photo of a dirty oven interior covered in burnt grease"></div>
    <div class="compare__shot compare__shot--after" role="img" aria-label="Photo of the same oven interior cleaned and shining"></div>
  </div>

  <div class="tag tag--before">BEFORE</div>
  <div class="tag tag--after">AFTER</div>

  <p class="cta-lead">Call Now for</p>
  <p class="cta-main">FAST, PROFESSIONAL SERVICE</p>

  <div class="phone phone--front">
    <span class="phone__icon">
      <svg width="26" height="26" viewBox="0 0 24 24" fill="none" stroke="var(--teal)" stroke-width="2" stroke-linecap="round" stroke-linejoin="round"><path d="M5 3h4l2 5-2.5 1.5a11 11 0 0 0 6 6L16 13l5 2v4a2 2 0 0 1-2 2A16 16 0 0 1 3 5a2 2 0 0 1 2-2"/></svg>
    </span>
    <span>0400 123 987</span>
  </div>
</section>

<section class="flyer flyer--back">
  <svg class="backdrop" viewBox="0 0 482 990" aria-hidden="true">
    <path d="M0 518 Q80 530 200 515 Q380 470 482 352 L482 990 L0 990 Z" fill="var(--teal)"/>
  </svg>

  <div class="brand"><span class="brand__dot"></span><span class="brand__name">Gleam Oven Care</span></div>

  <h2 class="headline headline--back">
    <span>WHY CHOOSE</span>
    <span class="sub">GLEAM OVEN CARE?</span>
  </h2>

  <ul class="reasons">
    <li>We're a local family business providing professional</li>
    <li>Non-caustic oven cleaning across Sunshine Coast.</li>
    <li>Using specialized-equipment and proven cleaning methods.</li>
    <li>We remove heavy grease, carbon build-up, smoke residue, restoring your oven safely and effectively.</li>
  </ul>

  <p class="offer-lead">Mention this flyer for</p>
  <p class="offer-main">$10 off your first clean</p>

  <div class="perks">
    <div class="perk">
      <div class="perk__badge">
        <svg width="52" height="52" viewBox="0 0 24 24" fill="none" stroke="#fff" stroke-width="1.6" stroke-linecap="round" stroke-linejoin="round"><circle cx="12" cy="12" r="9"/><path d="M7.5 12.5l3 3 6-6.5"/></svg>
      </div>
      <p class="perk__label">Reliable<br>Service</p>
    </div>
    <div class="perk">
      <div class="perk__badge">
        <svg width="52" height="52" viewBox="0 0 24 24" fill="none" stroke="#fff" stroke-width="1.6" stroke-linecap="round" stroke-linejoin="round"><rect x="3" y="3" width="18" height="18" rx="2"/><path d="M3 8h18"/><rect x="6.5" y="11" width="11" height="7" rx="1"/></svg>
      </div>
      <p class="perk__label">Non-Caustic<br>Cleaning</p>
    </div>
    <div class="perk">
      <div class="perk__badge">
        <svg width="52" height="52" viewBox="0 0 24 24" fill="none" stroke="#fff" stroke-width="1.6" stroke-linecap="round" stroke-linejoin="round"><path d="M12 3l7 3v5c0 5-3 8-7 10-4-2-7-5-7-10V6z"/><path d="M9 12l2 2 4-4"/></svg>
      </div>
      <p class="perk__label">Satisfaction<br>Guaranteed</p>
    </div>
  </div>

  <div class="contact">
    <div class="phone phone--back">
      <span class="phone__icon">
        <svg width="26" height="26" viewBox="0 0 24 24" fill="none" stroke="#fff" stroke-width="2" stroke-linecap="round" stroke-linejoin="round"><path d="M5 3h4l2 5-2.5 1.5a11 11 0 0 0 6 6L16 13l5 2v4a2 2 0 0 1-2 2A16 16 0 0 1 3 5a2 2 0 0 1 2-2"/></svg>
      </span>
      <span>0400 123 987</span>
    </div>
    <p class="contact__web">gleamovencare.com.au</p>
  </div>

  <p class="footnote">We also clean cooktops, rangehoods and BBQs</p>
</section>

</body>
</html>
```